Strength Coach Business Card Design Project

I would like a business card design to complement my new logo. I would like the card to be clean, seek and strong!

Target Market(s)

Mostly adults and junior atheletes who are serious about changing their lives.

Industry/Entity Type

Business

Font styles to use
Serif

Colors

Designer to choose colors to be used in the design.

```html
<!DOCTYPE html>
<html lang="en">
<head>
<meta charset="utf-8">
<title>Reed Strength and Fitness – Business Card</title>
<link rel="stylesheet" href="https://fonts.googleapis.com/css2?family=Oxanium:wght@500;700&family=Open+Sans:wght@400&display=swap">
<style>
  :root {
    --backdrop: #2a0b0b;
    --card: #ffffff;
    --ink: #333333;
    --ink-soft: #4a4a4a;
    --accent: #e3262e;
  }
  * { margin: 0; padding: 0; box-sizing: border-box; }
  html, body {
    width: 1200px;
    height: 800px;
    overflow: hidden;
    background: var(--backdrop);
  }
  .canvas {
    position: relative;
    width: 1200px;
    height: 800px;
  }
  .business-card {
    position: absolute;
    left: 180px;
    top: 160px;
    width: 840px;
    height: 480px;
    background: var(--card);
    box-shadow: 0 10px 30px rgba(0,0,0,0.45);
  }
  .brand {
    position: absolute;
    left: 70px;
    top: 120px;
    display: flex;
    align-items: center;
    gap: 22px;
  }
  .brand-mark {
    width: 70px;
    height: 70px;
    background: var(--accent);
  }
  .brand-name {
    font-family: "Oxanium", sans-serif;
    font-weight: 700;
    color: var(--ink);
    text-transform: uppercase;
    line-height: 0.95;
  }
  .brand-name .brand-main {
    display: block;
    font-size: 64px;
    letter-spacing: 2px;
  }
  .brand-name .brand-sub {
    display: block;
    font-size: 24px;
    letter-spacing: 1px;
  }
  .divider-band {
    position: absolute;
    left: 0;
    right: 0;
    top: 292px;
    height: 7px;
    background: var(--accent);
  }
  .holder {
    position: absolute;
    left: 70px;
    top: 316px;
  }
  .holder-name {
    font-family: "Oxanium", sans-serif;
    font-weight: 500;
    font-size: 34px;
    color: var(--accent);
    line-height: 1;
  }
  .holder-role {
    font-family: "Open Sans", sans-serif;
    font-size: 18px;
    color: var(--ink-soft);
    margin-top: 4px;
  }
  .contact-list {
    position: absolute;
    left: 70px;
    top: 388px;
    list-style: none;
  }
  .contact-item {
    display: flex;
    align-items: center;
    gap: 10px;
    font-family: "Oxanium", sans-serif;
    font-weight: 500;
    font-size: 24px;
    color: var(--ink);
    line-height: 1.2;
    margin-bottom: 2px;
  }
  .contact-icon {
    width: 20px;
    height: 20px;
    flex: none;
  }
</style>
</head>
<body>
<main class="canvas">
  <article class="business-card">
    <div class="brand">
      <div class="brand-mark"></div>
      <div class="brand-name">
        <span class="brand-main">Reed</span>
        <span class="brand-sub">Strength and Fitness</span>
      </div>
    </div>

    <div class="divider-band"></div>

    <div class="holder">
      <h1 class="holder-name">Marcus Reed</h1>
      <p class="holder-role">Strength and Fitness Coach</p>
    </div>

    <ul class="contact-list">
      <li class="contact-item">
        <svg class="contact-icon" viewBox="0 0 20 20" aria-hidden="true">
          <path d="M5 2 L8 2 L9 6 L7 8 Q9 12 12 13 L14 11 L18 12 L18 15 Q18 18 15 18 Q3 17 2 5 Q2 2 5 2 Z" fill="var(--accent)"/>
        </svg>
        0400 123 456
      </li>
      <li class="contact-item">
        <svg class="contact-icon" viewBox="0 0 20 20" aria-hidden="true">
          <circle cx="10" cy="10" r="9" fill="var(--accent)"/>
          <g fill="none" stroke="#fff" stroke-width="1.2">
            <circle cx="10" cy="10" r="6.5"/>
            <ellipse cx="10" cy="10" rx="3" ry="6.5"/>
            <line x1="3.5" y1="10" x2="16.5" y2="10"/>
          </g>
        </svg>
        www.marcus-reed.co
      </li>
      <li class="contact-item">
        <svg class="contact-icon" viewBox="0 0 20 20" aria-hidden="true">
          <rect x="1" y="4" width="18" height="13" rx="1.5" fill="var(--accent)"/>
          <path d="M2 5 L10 11 L18 5" fill="none" stroke="#fff" stroke-width="1.4"/>
        </svg>
        Coach@marcus-reed.co
      </li>
    </ul>
  </article>
</main>
</body>
</html>
```